" LOJA DO SEGMENTO DE AUTOPEÇAS, COM GONDOLAS EXPONDO ACESSORIOS AUTOMOTIVOS, PRODUTOS PARA ESTÉTICA E PINTURA DE AUTOMOVEIS , ALEM DA TRADICIONAL VENDA DE PEÇAS MECANICAS "

```html
<!DOCTYPE html>
<html lang="pt-BR">
<head>
<meta charset="utf-8">
<title>RODAMAX – Cartão de visita</title>
<link rel="stylesheet" href="https://fonts.googleapis.com/css2?family=Exo+2:wght@700;800&family=Roboto:wght@400;500&display=swap">
<style>
  :root {
    --bg: #e9e9e7;
    --card-dark: #0c0c0c;
    --card-light: #ffffff;
    --orange: #f26a21;
    --orange-soft: #f5a05a;
    --ink: #3a3a3a;
    --ink-soft: #666666;
    --white: #ffffff;
  }
  * { margin: 0; padding: 0; box-sizing: border-box; }
  html, body { width: 1200px; height: 1200px; overflow: hidden; }
  body {
    background: var(--bg);
    font-family: "Roboto", Arial, sans-serif;
    position: relative;
  }
  .card {
    position: absolute;
    width: 640px;
    height: 356px;
    border-radius: 22px;
    box-shadow: 0 6px 18px rgba(0,0,0,0.12);
    overflow: hidden;
  }
  /* Front */
  .card-front {
    left: 480px;
    top: 220px;
    background: var(--card-dark);
    display: flex;
    flex-direction: column;
    align-items: center;
    justify-content: center;
  }
  .brand {
    font-family: "Exo 2", Arial, sans-serif;
    font-weight: 800;
    letter-spacing: 2px;
    line-height: 1;
  }
  .card-front .brand { font-size: 72px; color: var(--white); display: flex; align-items: center; gap: 16px; }
  .brand-square { width: 22px; height: 22px; background: var(--orange); }
  .card-front .tagline {
    margin-top: 12px;
    font-size: 16px;
    letter-spacing: 3.5px;
    color: var(--orange);
    font-weight: 500;
  }
  /* Back */
  .card-back {
    left: 80px;
    top: 620px;
    background: var(--card-light);
  }
  .identity {
    position: absolute;
    left: 44px;
    top: 56px;
    display: flex;
    align-items: stretch;
  }
  .identity-brand { padding-right: 22px; }
  .card-back .brand { font-size: 46px; color: var(--ink); display: flex; align-items: center; gap: 10px; }
  .card-back .brand-square { width: 14px; height: 14px; }
  .card-back .tagline {
    margin-top: 6px;
    font-size: 9.5px;
    letter-spacing: 2.2px;
    color: var(--orange);
    font-weight: 500;
  }
  .divider { width: 3px; background: var(--orange); }
  .person { padding-left: 18px; display: flex; flex-direction: column; justify-content: center; }
  .person-name { font-size: 22px; color: var(--ink); font-weight: 500; }
  .person-role { font-size: 17px; color: var(--ink-soft); margin-top: 4px; }
  .contacts {
    position: absolute;
    left: 44px;
    top: 170px;
    display: grid;
    grid-template-columns: 230px 260px;
    row-gap: 14px;
    column-gap: 20px;
    font-size: 17px;
    color: var(--ink);
  }
  .contact { display: flex; align-items: center; gap: 8px; }
  .contact svg { width: 18px; height: 18px; flex: none; }
  .rule {
    position: absolute;
    left: 44px;
    right: 44px;
    top: 262px;
    height: 2px;
    background: linear-gradient(90deg, var(--orange-soft), var(--orange));
  }
  .rule-bottom {
    position: absolute;
    left: 44px;
    width: 400px;
    bottom: 34px;
    height: 1px;
    background: var(--orange);
  }
</style>
</head>
<body>

<section class="card card-front">
  <div class="brand"><span class="brand-square"></span>RODAMAX</div>
  <div class="tagline">PEÇAS E ACESSÓRIOS AUTOMOTIVOS</div>
</section>

<section class="card card-back">
  <div class="identity">
    <div class="identity-brand">
      <div class="brand"><span class="brand-square"></span>RODAMAX</div>
      <div class="tagline">PEÇAS E ACESSÓRIOS AUTOMOTIVOS</div>
    </div>
    <div class="divider"></div>
    <div class="person">
      <div class="person-name">Nome Sobrenome</div>
      <div class="person-role">Cargo</div>
    </div>
  </div>

  <div class="contacts">
    <div class="contact">
      <svg viewBox="0 0 24 24"><path fill="#f26a21" d="M12 2a7 7 0 0 0-7 7c0 5 7 13 7 13s7-8 7-13a7 7 0 0 0-7-7zm0 9.5A2.5 2.5 0 1 1 12 6.5a2.5 2.5 0 0 1 0 5z"/></svg>
      Coloque seu endereço aqui
    </div>
    <div class="contact">
      <svg viewBox="0 0 24 24"><rect x="2" y="5" width="20" height="14" rx="2" fill="#f26a21"/><path d="M3 6l9 7 9-7" stroke="#fff" stroke-width="1.8" fill="none"/></svg>
      contato@rodamax.com
    </div>
    <div class="contact">
      <svg viewBox="0 0 24 24"><path fill="#f26a21" d="M6.6 10.8a15 15 0 0 0 6.6 6.6l2.2-2.2a1 1 0 0 1 1-.25 11.4 11.4 0 0 0 3.6.57 1 1 0 0 1 1 1V20a1 1 0 0 1-1 1A17 17 0 0 1 3 4a1 1 0 0 1 1-1h3.5a1 1 0 0 1 1 1c0 1.25.2 2.45.57 3.6a1 1 0 0 1-.25 1z"/></svg>
      91 0000-0000
    </div>
    <div class="contact">
      <svg viewBox="0 0 24 24"><circle cx="12" cy="12" r="9" fill="#f26a21"/></svg>
      /rodamax
    </div>
  </div>

  <div class="rule"></div>
  <div class="rule-bottom"></div>
</section>

</body>
</html>
```